Beekeeper needs a label for honey jars

Ciao! I'm from Como Italy
I'm a hobbyist beekeeper and I produce honey for myself and my friends.
I've named my apiary "Teo di sole," a play on words between my nickname (Teo, from Matteo) and the Italian expression "Teo di sole," which translates to "a drizzle of honey" in English.
I need to create a label for my honey glass jars (250 gr and 500 gr).
I don't need a label for commercial purposes. I would like to include at least the name “Apicoltura Teo di sole", the type of honey (e.g., wildflower, acacia...) and a space for the production year, to be handwritten each year.
In the design some references to the world of bees.
For reference, attached a label with a style I like
Attached are the images of the selected jars and their measurements
Thanks and good job!

Target Market(s)

beekeeping, honey

Requirements
Nice to have
• I would like an elegant style with clean graphics.
Should not have
• Predominance of black color.

```html
<!DOCTYPE html>
<html lang="en">
<head>
<meta charset="utf-8">
<title>Apicoltura Teo Di Sole – Honey Label</title>
<link rel="stylesheet" href="https://fonts.googleapis.com/css2?family=Cutive&family=Rokkitt:wght@800&display=swap">
<style>
  :root {
    --paper: #ece9e6;
    --ink: #141414;
    --frame: #2b2a2a;
    --art-light: #dcd8d3;
    --art-dark: #c9c4be;
  }
  html, body {
    margin: 0;
    padding: 0;
    overflow: hidden;
    background: var(--paper);
  }
  .label {
    display: block;
    width: 1200px;
    height: 652px;
  }
  .label__bg { fill: var(--paper); }
  .label__rule {
    fill: none;
    stroke: var(--frame);
    stroke-width: 6;
  }
  .label__title {
    font-family: "Rokkitt", "Georgia", serif;
    font-weight: 800;
    font-size: 86px;
    fill: var(--ink);
  }
  .label__text {
    font-family: "Cutive", "Courier New", serif;
    fill: var(--ink);
  }
  .label__kicker { font-size: 40px; }
  .label__product { font-size: 112px; }
  .label__field-name { font-size: 60px; }
  .label__field-side { font-size: 40px; }
  .label__claim { font-size: 36px; }
  .label__write-line {
    stroke: var(--ink);
    stroke-width: 4.5;
    stroke-linecap: round;
    stroke-dasharray: 0 9.2;
  }
</style>
</head>
<body>
<svg class="label" viewBox="0 0 1200 652" xmlns="http://www.w3.org/2000/svg" aria-labelledby="label-title">
  <defs>
    <linearGradient id="bee-art-tone" x1="0" y1="0" x2="0" y2="1">
      <stop offset="0" stop-color="var(--art-light)"/>
      <stop offset="1" stop-color="var(--art-dark)"/>
    </linearGradient>
  </defs>

  <rect class="label__bg" width="1200" height="652"/>

  <!-- Frame and grid -->
  <rect class="label__rule" x="19" y="19" width="1162" height="614"/>
  <line class="label__rule" x1="19" y1="177" x2="1181" y2="177"/>
  <line class="label__rule" x1="218" y1="177" x2="218" y2="633"/>
  <line class="label__rule" x1="700" y1="177" x2="700" y2="633"/>
  <line class="label__rule" x1="218" y1="371" x2="700" y2="371"/>

  <!-- Apiary name -->
  <text id="label-title" class="label__title" x="61" y="130" textLength="1076" lengthAdjust="spacingAndGlyphs">Apicoltura Teo Di Sole</text>

  <!-- Handwritten fields, side column -->
  <g class="label__text label__field-side">
    <text transform="translate(91 617) rotate(-90)" textLength="147" lengthAdjust="spacingAndGlyphs">Season:</text>
    <text transform="translate(154 620) rotate(-90)" textLength="157" lengthAdjust="spacingAndGlyphs">Weight:</text>
  </g>
  <line class="label__write-line" x1="87" y1="430" x2="87" y2="196"/>
  <line class="label__write-line" x1="149" y1="428" x2="149" y2="201"/>

  <!-- Product name -->
  <text class="label__text label__kicker" x="343" y="231" textLength="230" lengthAdjust="spacingAndGlyphs">PURE RAW</text>
  <text class="label__text label__product" x="245" y="338" textLength="433" lengthAdjust="spacingAndGlyphs">HONEY</text>

  <!-- Bee illustration area -->
  <rect x="300" y="396" width="322" height="214" rx="6" fill="url(#bee-art-tone)" role="img" aria-label="Line illustration of a honey bee seen from above with spread wings"/>

  <!-- Honey type field -->
  <text class="label__text label__field-name" x="810" y="277" textLength="178" lengthAdjust="spacingAndGlyphs">Type:</text>
  <line class="label__write-line" x1="729" y1="411" x2="1146" y2="411"/>
  <line class="label__write-line" x1="729" y1="506" x2="1146" y2="506"/>

  <text class="label__text label__claim" x="724" y="589" textLength="429" lengthAdjust="spacingAndGlyphs">NATURAL PRODUCT</text>
</svg>
</body>
</html>
```